Kx7Orbit WebSite

an educational website about tutoring, client will be surfing this site looking for a tutor, please see the attached images because the contains exactly what we need.
Updates

Project Deadline Extended Reason: something went wrong with the uploaded files, we are very sorry.thank you PlumeVault for the 5 days extension.now there is a 3 images describing the content of the three pages.good luck Added Friday, August 5, 2016

Target Market(s)

everyone

Industry/Entity Type

Education

Number of Pages Required

3 page

Font styles to use
Other font styles liked:
• something looks good in Arabic and english like "Droid Arabic Kufi"

Requirements
Must have
• the logo we attached, responsive design, simple, also try as much as you can Centering texts and layout because this website will have an Arabic version, Arabic is a Right-to-Left Language.
• a change language button,
Nice to have
• educational gestures.
• Centered texts and layout because this website will have an Arabic version, Arabic is a Right-to-Left Language.
• we have a web designer and we can download any template and add our logo and text to it, but.....
• we need creativity, so please stick to the contents in the images we attached, we need something very simple, more like a zorvia home page with little touch of filtering fields like the 5 dropdownlist and the gender selection buttons.
• try not to go far away from the contents we specified in the images, use less images or dont use images at all, try not to make the client scroll down,
Should not have
• too much colors or noisy layout or heavy media

```html
<!DOCTYPE html>
<html lang="en">
<head>
<meta charset="utf-8">
<title>Kx7Orbit – Home</title>
<link rel="stylesheet" href="https://fonts.googleapis.com/css2?family=Lato:wght@400;700;900&family=Montserrat:wght@500;600&display=swap">
<style>
:root{
  --blue:#26a7e1;
  --blue-deep:#1175bf;
  --white:#ffffff;
  --ink:#1a1a1a;
  --footer:#0d0d0d;
  --divider:#5cc0ec;
  --fb:#3b5fc4;
  --tw:#12b3cf;
  --li:#0e8ac3;
  --gp:#d42424;
}
*{margin:0;padding:0;box-sizing:border-box}
html,body{width:1200px;height:693px;overflow:hidden;background:var(--white)}
body{position:relative;font-family:'Lato',sans-serif;color:var(--ink)}

.site-header{position:absolute;left:0;top:0;width:1200px;height:120px}
.nav-band{position:absolute;left:0;top:67px;width:1200px;height:53px;background:var(--blue)}
.header-shapes{position:absolute;left:0;top:0}
.brand{position:absolute;left:100px;top:22px;display:flex;align-items:center;gap:10px;z-index:2}
.brand-mark{width:38px;height:38px;background:var(--blue-deep)}
.brand-name{font-family:'Lato',sans-serif;font-weight:900;font-size:42px;color:var(--blue-deep);letter-spacing:-0.5px}

.contact-bar{position:absolute;top:20px;left:649px;display:flex;align-items:center;height:30px}
.contact-icon{width:30px;height:30px;background:var(--blue-deep);display:flex;align-items:center;justify-content:center}
.contact-text{font-weight:700;font-size:15.5px;margin-left:7px}
.contact-divider{width:1px;height:28px;background:var(--blue-deep);margin:0 13px 0 15px}
.lang-switch{position:absolute;left:1002px;top:18px;width:100px;height:35px;border:1px solid #7a7a7a;display:flex;align-items:center;padding-left:9px;font-size:13px;color:#333}
.lang-switch svg.flag{margin-right:9px}
.lang-switch svg.chev{margin-left:8px}

.main-nav{position:absolute;top:67px;left:0;width:1200px;height:53px}
.nav-item{position:absolute;top:0;height:53px;line-height:53px;color:var(--white);font-weight:700;font-size:14.5px;text-transform:uppercase;transform:translateX(-50%);white-space:nowrap}
.nav-sep{position:absolute;top:12px;width:1px;height:33px;background:var(--divider)}

.hero{position:absolute;left:0;top:120px;width:1200px;height:521px}
.hero-photo{position:absolute;inset:0;background:
  radial-gradient(ellipse 260px 300px at 330px 230px,#7a6458 0%,#4c3f39 55%,transparent 100%),
  radial-gradient(ellipse 300px 260px at 760px 300px,#4a4a44 0%,transparent 100%),
  linear-gradient(180deg,#3a3733 0%,#2d302a 55%,#3b3a30 100%)}
.hero-shade{position:absolute;inset:0;background:rgba(20,20,20,0.35)}
.slider-arrow{position:absolute;top:240px}
.hero-title{position:absolute;left:0;width:1200px;top:276px;text-align:center;font-family:'Montserrat',sans-serif;font-weight:600;font-size:33px;color:var(--white);letter-spacing:0.2px}
.filter-form{position:absolute;top:336px;left:321px;display:flex;height:50px}
.filter-select{width:179px;height:50px;background:var(--white);display:flex;align-items:center;justify-content:space-between;padding:0 14px 0 13px;font-family:'Montserrat',sans-serif;font-weight:600;font-size:15px;color:var(--ink)}
.filter-select + .filter-select{margin-left:15px}
.filter-submit{width:157px;height:50px;margin-left:10px;background:var(--blue-deep);color:var(--white);display:flex;align-items:center;justify-content:center;font-family:'Montserrat',sans-serif;font-weight:600;font-size:15px}

.site-footer{position:absolute;left:0;top:641px;width:1200px;height:52px;background:var(--footer)}
.copyright{position:absolute;left:100px;top:0;line-height:52px;font-size:11.5px;color:#e6e6e6}
.copyright strong{color:var(--white)}
.social-links{position:absolute;right:100px;top:11px;display:flex;gap:14px}
.social-dot{width:30px;height:30px;border-radius:50%}
.social-dot.fb{background:var(--fb)}
.social-dot.tw{background:var(--tw)}
.social-dot.li{background:var(--li)}
.social-dot.gp{background:var(--gp)}
</style>
</head>
<body>

<header class="site-header">
  <div class="nav-band"></div>
  <svg class="header-shapes" width="1200" height="120" viewBox="0 0 1200 120">
    <polygon points="0,67 64,67 96,120 0,120" fill="#26a7e1"/>
    <polygon points="64,0 373,0 373,67 340,120 96,120 64,67" fill="#ffffff"/>
    <polygon points="373,67 495,67 495,120 340,120" fill="#1175bf"/>
  </svg>

  <a class="brand">
    <span class="brand-mark"></span>
    <span class="brand-name">Kx7Orbit</span>
  </a>

  <div class="contact-bar">
    <span class="contact-icon">
      <svg width="16" height="16" viewBox="0 0 24 24"><path fill="#fff" d="M6.6 10.8a15.1 15.1 0 0 0 6.6 6.6l2.2-2.2a1 1 0 0 1 1-.25 11.4 11.4 0 0 0 3.6.57 1 1 0 0 1 1 1V20a1 1 0 0 1-1 1A17 17 0 0 1 3 4a1 1 0 0 1 1-1h3.5a1 1 0 0 1 1 1c0 1.25.2 2.45.57 3.57a1 1 0 0 1-.25 1z"/></svg>
    </span>
    <span class="contact-text">123-456-7890</span>
    <span class="contact-divider"></span>
    <span class="contact-icon">
      <svg width="16" height="12" viewBox="0 0 16 12"><path fill="#fff" d="M0 0h16v1.5L8 6.5 0 1.5z"/><path fill="#fff" d="M0 3.3l8 5 8-5V12H0z"/></svg>
    </span>
    <span class="contact-text">info@kx7orbit.com</span>
  </div>

  <div class="lang-switch">
    <svg class="flag" width="18" height="12" viewBox="0 0 18 12">
      <rect width="18" height="4" fill="#2a8c3c"/><rect y="4" width="18" height="4" fill="#fff"/><rect y="8" width="18" height="4" fill="#c8202f"/>
      <polygon points="0,0 5,4 5,8 0,12" fill="#111"/>
      <rect x="0.5" y="0.5" width="17" height="11" fill="none" stroke="#555" stroke-width="1"/>
    </svg>
    Arabic
    <svg class="chev" width="10" height="6" viewBox="0 0 10 6"><path d="M1 1l4 4 4-4" fill="none" stroke="#444" stroke-width="1.2"/></svg>
  </div>

  <nav class="main-nav">
    <a class="nav-item" style="left:434px">Home</a>
    <a class="nav-item" style="left:575px">About Us</a>
    <span class="nav-sep" style="left:657px"></span>
    <a class="nav-item" style="left:731px">Classes</a>
    <span class="nav-sep" style="left:807px"></span>
    <a class="nav-item" style="left:885px">Support</a>
    <span class="nav-sep" style="left:965px"></span>
    <a class="nav-item" style="left:1055px">Contact Us</a>
  </nav>
</header>

<section class="hero">
  <div class="hero-photo" role="img" aria-label="Photo of a smiling student with glasses in front of a blurred group of students outdoors"></div>
  <div class="hero-shade"></div>

  <svg class="slider-arrow" style="left:47px" width="18" height="40" viewBox="0 0 18 40"><path d="M16 2L3 20l13 18" fill="none" stroke="#fff" stroke-width="3.5"/></svg>
  <svg class="slider-arrow" style="left:1132px" width="18" height="40" viewBox="0 0 18 40"><path d="M2 2l13 18L2 38" fill="none" stroke="#fff" stroke-width="3.5"/></svg>

  <h1 class="hero-title">Providing Safe and Educational Enviroument</h1>

  <form class="filter-form">
    <div class="filter-select">Subject
      <svg width="11" height="6" viewBox="0 0 11 6"><path d="M0 0h11L5.5 6z" fill="#111"/></svg>
    </div>
    <div class="filter-select">Gender
      <svg width="11" height="6" viewBox="0 0 11 6"><path d="M0 0h11L5.5 6z" fill="#111"/></svg>
    </div>
    <div class="filter-submit">Submit</div>
  </form>
</section>

<footer class="site-footer">
  <p class="copyright">COPYRIGHT © 2016 <strong>Kx7Orbit</strong> | ALL RIGHT RESERVED.</p>
  <div class="social-links">
    <span class="social-dot fb"></span>
    <span class="social-dot tw"></span>
    <span class="social-dot li"></span>
    <span class="social-dot gp"></span>
  </div>
</footer>

</body>
</html>
```